Corvanta Business cards template

We're looking for something modern and elegant. We are a reseller of technology (computers, datacenter, etc). Color theme would be "only" white with the incorporation of the blue that's present on our website (Corvanta.com) and logo file. We would like for the card to provide all the necessary info for the specific person (Phone#, fax#, email, name, website URL) . I'm attaching the logo file to this request. Please have it show Easthaven/Lakemont somewhere, without providing specific addresses.

Target Market(s)

All b2b

Industry/Entity Type

Business

Contact Information for Business Card

Please have the color scheme be represented by only the white and blue from our website (Corvanta.com) and logo. We would like to logo on the card, but not big and overwhelming. This card will be used as a template for anybody within the company, it should display the user's name, phone#, fax#, email, job title and website URL. Please have it show Easthaven/Lakemont somewhere, without providing our specific addresses. Really, we're looking for a clean, simple and elegant look.

Font styles to use
Serif

Requirements
Must have
• Please see card details
Nice to have
• Please see card details
Should not have
• Anything tacky or tagline.

```html
<!DOCTYPE html>
<html lang="en">
<head>
<meta charset="utf-8">
<title>Corvanta Business Card</title>
<link rel="stylesheet" href="https://fonts.googleapis.com/css2?family=Quicksand:wght@500&family=Fira+Sans+Condensed:ital,wght@0,300;1,300&display=swap">
<style>
  :root {
    --page: #ffffff;
    --blue: #47ade0;
    --blue-deep: #3b9dd2;
    --brand: #0b7cc5;
    --white: #ffffff;
    --mist-a: #fbfbfb;
    --mist-b: #ececec;
  }
  * { margin: 0; padding: 0; box-sizing: border-box; }
  html, body { width: 1200px; height: 1200px; overflow: hidden; background: var(--page); }
  .canvas { position: relative; width: 1200px; height: 1200px; }

  .card {
    position: absolute;
    left: 180px;
    width: 840px;
    height: 480px;
    overflow: hidden;
    background: linear-gradient(135deg, var(--mist-a) 0%, var(--mist-b) 55%, var(--mist-a) 100%);
  }
  .card-front { top: 90px; }
  .card-back { top: 638px; }

  .band {
    position: absolute;
    left: 0;
    width: 100%;
    background: linear-gradient(110deg, var(--blue-deep) 0%, var(--blue) 45%, var(--blue-deep) 100%);
  }
  .band-top { top: 0; height: 96px; }
  .band-bottom {
    top: 396px; height: 84px;
    display: flex; align-items: center; justify-content: center;
  }
  .cities {
    font-family: "Quicksand", sans-serif;
    font-weight: 500;
    font-size: 26px;
    color: var(--white);
    transform: translateY(-2px);
  }
  .brand-name {
    position: absolute;
    top: 178px;
    left: 0;
    width: 100%;
    text-align: center;
    font-family: "Quicksand", sans-serif;
    font-weight: 500;
    font-size: 104px;
    line-height: 1;
    color: var(--brand);
  }

  .back-art { position: absolute; inset: 0; width: 840px; height: 480px; }

  .field {
    position: absolute;
    left: 280px;
    font-family: "Fira Sans Condensed", sans-serif;
    font-weight: 300;
    font-size: 30px;
    color: var(--white);
    letter-spacing: 0.5px;
  }
  .field-name { top: 108px; }
  .field-title { top: 168px; }

  .contact {
    position: absolute;
    top: 294px;
    left: 234px;
    width: 300px;
    text-align: center;
    font-family: "Fira Sans Condensed", sans-serif;
    font-style: italic;
    font-weight: 300;
    font-size: 30px;
    line-height: 40px;
    color: var(--white);
  }
  .brand-small {
    position: absolute;
    left: 24px;
    top: 424px;
    font-family: "Quicksand", sans-serif;
    font-weight: 500;
    font-size: 22px;
    color: var(--brand);
  }
  .website {
    position: absolute;
    right: 16px;
    top: 444px;
    font-family: "Quicksand", sans-serif;
    font-weight: 500;
    font-size: 25px;
    color: var(--white);
  }
</style>
</head>
<body>
<main class="canvas">
  <section class="card card-front">
    <div class="band band-top"></div>
    <div class="brand-name">Corvanta</div>
    <div class="band band-bottom"><span class="cities">Easthaven/Lakemont</span></div>
  </section>

  <section class="card card-back">
    <svg class="back-art" viewBox="0 0 840 480" aria-hidden="true">
      <defs>
        <linearGradient id="wave-fill" x1="0" y1="0" x2="1" y2="1">
          <stop offset="0" stop-color="#3c9fd4"/>
          <stop offset="0.5" stop-color="#48aee0"/>
          <stop offset="1" stop-color="#3d9fd3"/>
        </linearGradient>
      </defs>
      <path class="wave" d="M92 0 C60 80 55 220 200 300 C290 352 330 400 354 480 L840 480 L840 0 Z" fill="url(#wave-fill)"/>
      <path class="pill" d="M840 86 H284 A68 68 0 0 0 284 222 H840" fill="none" stroke="#ffffff" stroke-width="3"/>
      <line class="divider" x1="254" y1="152" x2="840" y2="152" stroke="#ffffff" stroke-width="3"/>
    </svg>
    <div class="field field-name">NAME:</div>
    <div class="field field-title">JOB&nbsp; TITLE:</div>
    <div class="contact">
      <div>TELEPHONE NUMBER:</div>
      <div>FAX NUMBER:</div>
      <div>EMAIL:</div>
    </div>
    <div class="brand-small">Corvanta</div>
    <div class="website">Corvanta.com</div>
  </section>
</main>
</body>
</html>
```